Author and Publisher

Cover for a book on the process of publishing a book from the presentation to the publisher until the selling in bookstores :
A behind-the-scenes journey through the world of book publishing, from manuscript to bookstore. The book explores the relationship between authors and publishers, manuscript selection, contracts, editing, proofreading, book design, printing, distribution, bookstores and online sales. It reveals the many people, decisions and processes involved in turning a text into a physical book and bringing it to readers. The illustration should evoke publishing as a lively, contemporary ecosystem, combining creativity, craftsmanship, business and the enduring appeal of books.
FORMAT : 14 x 20,5 cm
AUTHOR : Luc Varennes
TITLE : Le scribe et la presse
PUBLISHER : Editions Trovel (at the bottom of the page)
Target Market(s)
General public, mainly news authors of books
Look and feel
Each slider illustrates characteristics of the customer's brand and the style your logo design should communicate.

```html
<!DOCTYPE html>
<html lang="fr">
<head>
<meta charset="utf-8">
<title>Le scribe et la presse — Luc Varennes</title>
<link href="https://fonts.googleapis.com/css2?family=Playfair+Display:wght@700;900&family=Figtree:wght@400;500&family=EB+Garamond:wght@500&display=swap" rel="stylesheet">
<style>
  :root{
    --page:#ffffff;
    --ink:#0f1a2b;
    --red:#c3281c;
    --slate:#5d6b78;
    --wall-top:#f7f6f2;
    --wall-bottom:#eeebe4;
    --shelf-dark:#2e2520;
    --shelf-mid:#6b5443;
    --desk-top:#7a4a2b;
    --desk-light:#9a643d;
    --desk-front:#3f2314;
    --paper:#f2eee6;
    --paper-shade:#cfc6b8;
    --caption:#f4ede4;
  }
  *{margin:0;padding:0;box-sizing:border-box}
  html,body{width:944px;height:1200px;overflow:hidden;background:var(--page)}
  .cover{
    position:absolute;left:82px;top:30px;width:779px;height:1140px;overflow:hidden;
    background:linear-gradient(180deg,var(--wall-top),var(--wall-bottom));
  }
  .scene-shelves{
    position:absolute;left:653px;top:0;width:126px;height:861px;
    background:linear-gradient(180deg,var(--shelf-dark) 0%,var(--shelf-mid) 45%,#8a7260 70%,var(--shelf-mid) 100%);
  }
  .scene-plant{
    position:absolute;left:0;top:370px;width:150px;height:380px;
    background:radial-gradient(ellipse at 40% 40%,#4f6e3e 0%,rgba(79,110,62,.55) 45%,rgba(79,110,62,0) 72%);
  }
  .scene-desk{
    position:absolute;left:0;top:861px;width:779px;height:152px;
    background:linear-gradient(180deg,var(--desk-light),var(--desk-top));
  }
  .scene-desk-front{
    position:absolute;left:0;top:1013px;width:779px;height:127px;
    background:linear-gradient(180deg,#4b2a18,var(--desk-front));
  }
  .scene-pages{
    position:absolute;left:0;top:560px;width:707px;height:340px;
    border-radius:6px 40px 4px 4px;
    background:linear-gradient(100deg,var(--paper) 0%,#ece6da 40%,var(--paper-shade) 62%,#8ea0a8 82%,#4e6a55 100%);
  }
  .author{
    position:absolute;top:36px;left:0;width:100%;text-align:center;
    font-family:"Playfair Display",serif;font-weight:700;font-size:36px;letter-spacing:4px;color:var(--ink);
  }
  .rule{position:absolute;left:349px;width:80px;height:2px;background:var(--red)}
  .rule-top{top:104px}
  .rule-mid{top:473px}
  .title{
    position:absolute;left:0;width:100%;text-align:center;
    font-family:"Playfair Display",serif;font-weight:900;line-height:1;letter-spacing:-2px;
  }
  .title-line1{top:146px;font-size:112px;color:var(--ink)}
  .title-line2{top:248px;font-size:104px;color:var(--red)}
  .title-line2 .joiner{font-size:58px;color:var(--slate);letter-spacing:0;margin-right:14px}
  .subtitle{
    position:absolute;top:385px;left:0;width:100%;text-align:center;
    font-family:"Figtree",sans-serif;font-size:23px;line-height:31px;color:#1b1f24;
  }
  .verbs{
    position:absolute;left:164px;top:492px;list-style:none;
    font-family:"Figtree",sans-serif;font-weight:500;font-size:11px;letter-spacing:4px;line-height:26px;color:var(--slate);
  }
  .badge{
    position:absolute;left:570px;top:449px;width:122px;height:122px;border-radius:50%;background:var(--red);
    display:flex;align-items:center;justify-content:center;text-align:center;
    font-family:"Playfair Display",serif;font-weight:700;font-size:15px;line-height:18px;color:#fff;
  }
  .steps{position:absolute;left:0;top:910px;width:100%;height:40px}
  .step{
    position:absolute;top:0;transform:translateX(-50%);text-align:center;
    font-family:"Figtree",sans-serif;font-weight:500;font-size:10px;letter-spacing:.8px;color:var(--caption);
  }
  .step::before{content:"";display:block;width:24px;height:1px;margin:0 auto 18px;background:var(--caption);opacity:.7}
  .publisher{
    position:absolute;top:1060px;left:0;width:100%;text-align:center;
    font-family:"EB Garamond",serif;font-weight:500;font-size:26px;letter-spacing:-.3px;color:#f6efe6;
  }
</style>
</head>
<body>
  <main class="cover">
    <div class="scene-shelves" role="img" aria-label="Rayonnages de librairie chargés de livres, flous à l'arrière-plan"></div>
    <div class="scene-plant" role="img" aria-label="Plante verte et pot à crayons sur le bureau"></div>
    <div class="scene-desk" role="img" aria-label="Plateau de bureau en bois"></div>
    <div class="scene-desk-front"></div>
    <div class="scene-pages" role="img" aria-label="Manuscrit empilé dont les pages s'envolent et se transforment en livres ouverts illustrés d'un paysage de montagne"></div>

    <p class="author">Luc Varennes</p>
    <span class="rule rule-top"></span>

    <h1>
      <span class="title title-line1">Le scribe</span>
      <span class="title title-line2"><span class="joiner">et</span>la presse</span>
    </h1>

    <p class="subtitle">Dans les coulisses du livre,<br>de l'idée au lecteur</p>
    <span class="rule rule-mid"></span>

    <ul class="verbs">
      <li>CRÉER</li>
      <li>ÉDITER</li>
      <li>FABRIQUER</li>
      <li>DIFFUSER</li>
      <li>PARTAGER</li>
    </ul>

    <div class="badge">Un<br>monde<br>de possibles</div>

    <div class="steps">
      <span class="step" style="left:96px">MANUSCRIT</span>
      <span class="step" style="left:216px">ÉDITION</span>
      <span class="step" style="left:324px">CONCEPTION</span>
      <span class="step" style="left:442px">IMPRESSION</span>
      <span class="step" style="left:558px">LIBRAIRIE</span>
      <span class="step" style="left:675px">LECTEURS</span>
    </div>

    <p class="publisher">Éditions Trovel</p>
  </main>
</body>
</html>
```